Website for new crypto research organization

See brief (attached). This is a pretty basic website with only a handful of pages + ability to collect email addresses.

```html
<!DOCTYPE html>
<html lang="en">
<head>
<meta charset="utf-8">
<title>Cyanline Research</title>
<link rel="stylesheet" href="https://fonts.googleapis.com/css2?family=Space+Grotesk:wght@400;500;600&family=Inter:wght@400;500&display=swap">
<style>
  :root {
    --teal: #03a9a2;
    --ink: #161616;
    --muted: #5a5a5a;
    --stage: #e4e4e4;
    --band: #eeeeee;
    --paper: #f6f6f6;
    --line: #c8c8c8;
    --deep: #0e4a5c;
    --display: "Space Grotesk", sans-serif;
    --body: "Inter", sans-serif;
  }
  * { box-sizing: border-box; margin: 0; padding: 0; }
  html, body { width: 1200px; height: 3458px; overflow: hidden; }
  body { background: var(--stage); font-family: var(--body); color: var(--ink); }

  .site { position: absolute; left: 0; top: 294px; width: 1200px; height: 2870px; background: var(--paper); }
  section, header, footer { position: relative; width: 1200px; }

  .brand { position: absolute; display: flex; align-items: center; gap: 8px; font-family: var(--display); font-weight: 500; font-size: 20px; color: var(--teal); }
  .brand-mark { width: 14px; height: 14px; background: var(--teal); }

  .topbar { height: 100px; background: var(--band); border-bottom: 1px solid #e2e2e2; }
  .topbar .brand { left: 162px; top: 36px; }
  .menu { position: absolute; left: 672px; top: 38px; display: flex; gap: 0; list-style: none; font-size: 12px; color: #333; }
  .menu li { width: 74px; text-align: center; }
  .menu li:last-child { width: 80px; text-align: right; }
  .menu .is-active { color: var(--teal); }
  .menu .is-active span { border-bottom: 1px solid var(--teal); padding-bottom: 5px; }

  .hero { height: 669px; background: linear-gradient(90deg, #f5f5f5 0%, #f3f3f3 25%, #dcdfe0 55%, #c7cbcd 75%, #1a5a6d 88%, var(--deep) 100%); overflow: hidden; }
  .hero-art { position: absolute; inset: 0; }
  .hero-title { position: absolute; left: 162px; top: 250px; font-family: var(--display); font-weight: 500; font-size: 39px; line-height: 52px; letter-spacing: 0.3px; }
  .hero-title mark { background: var(--teal); color: #fff; padding: 0 5px; }
  .hero-title .dot { color: var(--teal); }

  .about { height: 743px; background: var(--paper); }
  .about h2 { font-family: var(--display); font-weight: 500; font-size: 27px; }
  .about h3 { font-family: var(--display); font-weight: 500; font-size: 21px; }
  .about p { font-size: 11px; line-height: 22px; color: var(--muted); width: 430px; }
  .block { position: absolute; left: 162px; }
  .block h2, .block h3 { margin-bottom: 12px; }
  .link-more { font-family: var(--display); font-size: 14px; color: var(--teal); display: flex; align-items: center; gap: 12px; }
  .about .link-more { position: absolute; left: 162px; top: 228px; }
  .globe { position: absolute; left: 722px; top: 200px; width: 350px; height: 350px; border-radius: 50%; background: radial-gradient(circle, #f3f3f3 30%, #e6e8e8 70%, #f6f6f6 100%); }
  .globe-name { position: absolute; left: 722px; top: 356px; width: 350px; text-align: center; font-family: var(--display); font-weight: 600; font-size: 40px; color: var(--teal); }

  .research-head { height: 228px; background: var(--band); }
  .research-head h2 { position: absolute; left: 162px; top: 97px; font-family: var(--display); font-weight: 500; font-size: 27px; }
  .btn-outline { position: absolute; left: 912px; top: 89px; width: 127px; height: 49px; border: 1px solid var(--teal); color: var(--teal); font-size: 10px; display: flex; align-items: center; justify-content: center; letter-spacing: 0.3px; }

  .cards { height: 526px; display: flex; }
  .card { position: relative; width: 400px; height: 526px; background: var(--paper); }
  .card.is-featured { background: var(--teal); color: #fff; }
  .card-date { position: absolute; left: 60px; top: 88px; font-size: 11px; color: #444; }
  .card-tags { position: absolute; left: 60px; top: 114px; display: flex; gap: 5px; list-style: none; }
  .card-tags li { width: 89px; height: 25px; border: 1px solid var(--line); font-size: 9px; display: flex; align-items: center; justify-content: center; color: #444; }
  .card-title { position: absolute; left: 60px; top: 168px; font-family: var(--display); font-weight: 500; font-size: 21px; line-height: 25px; }
  .card .link-more { position: absolute; left: 58px; top: 424px; }
  .is-featured .card-date, .is-featured .card-tags li, .is-featured .link-more { color: #fff; }
  .is-featured .card-tags li { border-color: rgba(255,255,255,0.7); }

  .subscribe { height: 235px; background: var(--band); }
  .subscribe h2 { position: absolute; left: 162px; top: 86px; font-family: var(--display); font-weight: 500; font-size: 27px; line-height: 33px; }
  .signup { position: absolute; left: 636px; top: 97px; display: flex; }
  .signup-field { width: 276px; height: 48px; border: 1px solid var(--teal); background: #fff; font-size: 10px; color: #999; padding-left: 20px; display: flex; align-items: center; }
  .signup-button { width: 127px; height: 48px; background: var(--teal); color: #fff; font-size: 10px; font-weight: 500; display: flex; align-items: center; justify-content: center; }

  .footer { height: 369px; background: var(--paper); }
  .footer .brand { left: 162px; top: 108px; }
  .disclaimer { position: absolute; left: 162px; top: 172px; width: 360px; font-size: 10.5px; line-height: 22px; color: #444; }
  .footer h4 { position: absolute; top: 89px; font-family: var(--display); font-weight: 500; font-size: 15px; }
  .rule { position: absolute; top: 128px; width: 38px; height: 1px; background: var(--teal); }
  .quick-links { position: absolute; left: 683px; top: 153px; list-style: none; font-size: 11px; color: #444; line-height: 29px; }
  .socials { position: absolute; left: 934px; top: 156px; display: flex; gap: 9px; }
  .socials span { width: 29px; height: 29px; background: var(--teal); }
</style>
</head>
<body>
<div class="site">
  <header class="topbar">
    <div class="brand"><span class="brand-mark"></span>Cyanline Research</div>
    <ul class="menu">
      <li class="is-active"><span>Home</span></li>
      <li>About</li>
      <li>Research</li>
      <li>Careers</li>
      <li>News</li>
      <li>Contact</li>
    </ul>
  </header>

  <section class="hero">
    <div class="hero-art" role="img" aria-label="Illustration of a person pulling back a grey curtain to reveal a dark teal wall of glowing crypto coins"></div>
    <h1 class="hero-title">Cyanline <mark>Research</mark><br>is a research-driven<br>digital asset<span class="dot">.</span></h1>
  </section>

  <section class="about">
    <div class="block" style="top:92px">
      <h2>About Us</h2>
      <p>Lorem ipsum dolor sit amet, consectetur adipiscing elit, sed do eiusmod tempor incididunt ut labore et dolore magna aliqua. Quis ipsum suspendisse ultrices gravida. Risus commodo viverra maecenas accumsan lacus vel.</p>
    </div>
    <a class="link-more">Meet our team
      <svg width="18" height="10" viewBox="0 0 18 10"><path d="M0 5h16M12 1l4 4-4 4" fill="none" stroke="currentColor" stroke-width="1.3"/></svg></a>
    <div class="block" style="top:330px">
      <h3>Who we are</h3>
      <p>A thematic, research-driven digital asset investment firm built for founders.</p>
    </div>
    <div class="block" style="top:442px">
      <h3>Vision</h3>
      <p>Web3, blockchain technology, and digital assets will drive the largest wealth shift in the global economy since the advent of the internet</p>
    </div>
    <div class="block" style="top:575px">
      <h3>Mission</h3>
      <p>We apply a principled digital asset investment strategy and partner with founders to enable their token-based decentralized networks to scale</p>
    </div>
    <div class="globe" role="img" aria-label="Faint wireframe globe decoration"></div>
    <div class="globe-name">Cyanline</div>
  </section>

  <section class="research-head">
    <h2>Research</h2>
    <a class="btn-outline">DISCOVER MORE</a>
  </section>

  <section class="cards">
    <article class="card">
      <div class="card-date">07/02/2022</div>
      <ul class="card-tags"><li>RESEARCH</li><li>CRYPTO</li><li>BLOCKCHAIN</li></ul>
      <h3 class="card-title">Lorem ipsum dolor sitot:<br>Consectetur adipiscinget</h3>
      <a class="link-more">read more <svg width="18" height="10" viewBox="0 0 18 10"><path d="M0 5h16M12 1l4 4-4 4" fill="none" stroke="currentColor" stroke-width="1.3"/></svg></a>
    </article>
    <article class="card is-featured">
      <div class="card-date">07/02/2022</div>
      <ul class="card-tags"><li>RESEARCH</li><li>CRYPTO</li><li>BLOCKCHAIN</li></ul>
      <h3 class="card-title">Lorem ipsum dolor sitot:<br>Consectetur adipiscinget</h3>
      <a class="link-more">read more <svg width="18" height="10" viewBox="0 0 18 10"><path d="M0 5h16M12 1l4 4-4 4" fill="none" stroke="currentColor" stroke-width="1.3"/></svg></a>
    </article>
    <article class="card">
      <div class="card-date">07/02/2022</div>
      <ul class="card-tags"><li>RESEARCH</li><li>CRYPTO</li><li>BLOCKCHAIN</li></ul>
      <h3 class="card-title">Lorem ipsum dolor sitot:<br>Consectetur adipiscinget</h3>
      <a class="link-more">read more <svg width="18" height="10" viewBox="0 0 18 10"><path d="M0 5h16M12 1l4 4-4 4" fill="none" stroke="currentColor" stroke-width="1.3"/></svg></a>
    </article>
  </section>

  <section class="subscribe">
    <h2>Subscribe To<br>Cyanline Research</h2>
    <div class="signup">
      <div class="signup-field">Type your email address here</div>
      <div class="signup-button">SUBSCRIBE</div>
    </div>
  </section>

  <footer class="footer">
    <div class="brand"><span class="brand-mark"></span>Cyanline Research</div>
    <p class="disclaimer">This site is not intended to provide any investment, financial, legal, regulatory, accounting, tax or similar advice, and nothing on this site should be construed as a recommendation by Cyanline Research, its affiliates, or any third party, to acquire or dispose of any investment, or to engage in any investment strategy or transaction.</p>
    <h4 style="left:683px">Quick Links</h4>
    <div class="rule" style="left:683px"></div>
    <ul class="quick-links"><li>About</li><li>Research</li><li>Careers</li><li>Team</li><li>Contact</li></ul>
    <h4 style="left:934px">Follow Us</h4>
    <div class="rule" style="left:934px"></div>
    <div class="socials" aria-label="Social links"><span></span><span></span><span></span></div>
  </footer>
</div>
</body>
</html>
```